Business Card Design Project

Business card design for an IT Service company. A logo has already been created in a different contest and has been attached to this project. Ideally we're looking for a double sided business card that matches the look and feel of our newly created logo.

We're open to creativity if you feel a tag line is needed such as "IT Services and Application Development". We're open to really and look and feel - even single sided business cards if you feel you have something that's a great idea.

Last thought here - I'm not sure how it'll look but maybe a two tone card? One side dark blue and the other side white? Don't limit the design submissions to this tho - just curious if it would look good

Nothing too busy please - simple... Thank you and happy designing!

Target Market(s)

Businesses that require IT Services and support for hosted services, technical consultation, web design.

Industry/Entity Type

Business

Font styles to use
Sans Serif

Requirements
Must have
• Use the colors provided in the logo (see attachment) or additional colors that compliment
Must have the following contact info (not necessarily in this order):
- Owen Marsh
- Founding Partner
- omarsh@velomarquin.com
- 555-271-3948
- www.velomarquin.com

```html
<!DOCTYPE html>
<html lang="en">
<head>
<meta charset="utf-8">
<title>Velomarquin Business Card</title>
<link rel="stylesheet" href="https://fonts.googleapis.com/css2?family=Open+Sans:wght@400;600;700&display=swap">
<style>
  :root {
    --page-bg: #e6e7ea;
    --navy: #23305e;
    --navy-deep: #1c2750;
    --navy-light: #3a4f86;
    --circuit-green: #7a9a3c;
    --circuit-blue: #4f86c6;
    --card-white: #ffffff;
    --text-navy: #1f2a52;
    --white: #ffffff;
  }
  * { box-sizing: border-box; margin: 0; padding: 0; }
  html, body {
    width: 1200px;
    height: 800px;
    overflow: hidden;
    background: var(--page-bg);
    font-family: "Open Sans", Arial, sans-serif;
  }
  .canvas {
    position: relative;
    width: 1200px;
    height: 800px;
  }
  .card {
    position: absolute;
    top: 246px;
    width: 540px;
    height: 308px;
    border-radius: 4px;
    box-shadow: 0 6px 18px rgba(0, 0, 0, 0.18);
    overflow: hidden;
  }
  .card-front {
    left: 40px;
    background: var(--card-white);
    border: 4px solid var(--navy);
    color: var(--text-navy);
  }
  .contact {
    position: absolute;
    top: 26px;
    left: 32px;
  }
  .contact-name {
    font-size: 21px;
    font-weight: 700;
    line-height: 1.1;
  }
  .contact-title {
    font-size: 14px;
    font-weight: 400;
    margin-bottom: 14px;
  }
  .contact-line {
    font-size: 14px;
    line-height: 1.4;
  }
  .contact-line .label { font-weight: 700; }
  .contact-web {
    margin-top: 18px;
    font-size: 14px;
    font-weight: 700;
  }
  .brand {
    position: absolute;
    right: 30px;
    bottom: 78px;
    display: flex;
    align-items: center;
    gap: 10px;
  }
  .brand-mark {
    width: 22px;
    height: 22px;
    background: var(--circuit-blue);
  }
  .brand-name {
    font-size: 34px;
    font-weight: 700;
    color: var(--navy);
    letter-spacing: -0.5px;
  }
  .card-back {
    right: 40px;
    background: linear-gradient(160deg, var(--navy-light) 0%, var(--navy) 55%, var(--navy-deep) 100%);
    border: 4px solid var(--navy-deep);
  }
  .circuit-band {
    position: absolute;
    top: 0;
    left: 0;
    width: 300px;
    height: 150px;
    background: linear-gradient(135deg, var(--circuit-green) 0%, var(--circuit-blue) 55%, rgba(58, 79, 134, 0) 100%);
    opacity: 0.85;
  }
  .tagline {
    position: absolute;
    right: 34px;
    bottom: 36px;
    font-size: 17px;
    font-weight: 400;
    color: var(--white);
  }
</style>
</head>
<body>
  <main class="canvas">
    <section class="card card-front" aria-label="Business card front">
      <div class="contact">
        <p class="contact-name">Owen Marsh</p>
        <p class="contact-title">Founding Partner</p>
        <p class="contact-line"><span class="label">T:</span> 555-271-3948</p>
        <p class="contact-line"><span class="label">E:</span> omarsh@velomarquin.com</p>
        <p class="contact-web">www.velomarquin.com</p>
      </div>
      <div class="brand">
        <span class="brand-mark"></span>
        <span class="brand-name">Velomarquin</span>
      </div>
    </section>

    <section class="card card-back" aria-label="Business card back">
      <div class="circuit-band" role="img" aria-label="Green and blue circuit-line decoration from the brand symbol"></div>
      <p class="tagline">IT Services and Application Development</p>
    </section>
  </main>
</body>
</html>
```